Embroidery Teacher

I design and teach small embroidery classes, I am based in South Australia
The majority of my embroidery is done on bright wool fabrics and the designs are naive / folk art type birds, flowers and houses. The finished products stitched by the ladies in my classes are usually made into book covers, needle keepers or small quilts.

Industry/Entity Type

Embroidery

Contact Information for Business Card

Rosalind Harker
PO Box 3817
Ashgrove Vale SA 5092
M. 0428361957
E. roz@cosyneedlework.com.au

```html
<!DOCTYPE html>
<html lang="en">
<head>
<meta charset="utf-8">
<title>Rosalind Harker — Business Card</title>
<link href="https://fonts.googleapis.com/css2?family=Cinzel:wght@700&family=Handlee&family=Schoolbell&display=block" rel="stylesheet">
<style>
  :root {
    --page: #ffffff;
    --lime: #dfe79b;
    --ink: #1e1a17;
    --orange: #f6a21e;
    --orange-deep: #ef7f1a;
    --orange-light: #f9bd3a;
    --felt-purple: #3a1f5c;
    --felt-mustard: #d8c26a;
    --felt-orange: #f08a1c;
    --felt-plum: #6e2355;
  }
  * { margin: 0; padding: 0; box-sizing: border-box; }
  html, body { width: 1200px; height: 1000px; overflow: hidden; background: var(--page); }
  .canvas { position: relative; width: 1200px; height: 1000px; }

  .card { position: absolute; left: 304px; width: 593px; overflow: hidden; }
  .card-front { top: 143px; height: 348px; background: var(--lime); }
  .card-back {
    top: 512px; height: 347px;
    background: linear-gradient(135deg, var(--orange-light) 0%, var(--orange) 45%, var(--orange-deep) 100%);
  }

  .showcase { position: absolute; left: 0; top: 0; width: 593px; height: 230px; }

  .name {
    position: absolute; left: 0; right: 0; top: 240px;
    text-align: center;
    font-family: "Cinzel", serif; font-weight: 700;
    font-size: 31px; letter-spacing: 0.5px; color: var(--ink);
  }
  .role {
    position: absolute; left: 0; right: 0; top: 292px;
    text-align: center;
    font-family: "Schoolbell", "Handlee", cursive;
    font-weight: 400;
    font-size: 27px; letter-spacing: 1.5px; color: var(--ink);
  }

  .work-feature {
    position: absolute; right: 0; top: 0; width: 225px; height: 347px;
    background: radial-gradient(circle at 55% 50%, #4a2a6e 0%, var(--felt-purple) 70%, #2a1645 100%);
    box-shadow: -14px 0 24px rgba(239,127,26,0.8);
  }

  .contact {
    position: absolute; left: 27px; top: 145px;
    font-family: "Cinzel", serif; font-weight: 700; color: var(--ink);
    list-style: none;
  }
  .contact li { font-size: 25px; line-height: 43px; }
  .contact .email { font-size: 16px; line-height: 34px; }
</style>
</head>
<body>
<div class="canvas">

  <section class="card card-front">
    <svg class="showcase" viewBox="0 0 593 230" width="593" height="230">
      <g fill="none" stroke="var(--ink)">
        <circle cx="114" cy="90" r="88" stroke-width="1.6" stroke-dasharray="4 3"/>
        <circle cx="298" cy="122" r="88" stroke-width="1.6" stroke-dasharray="4 3"/>
        <circle cx="479" cy="90" r="88" stroke-width="1.6" stroke-dasharray="4 3"/>
        <circle cx="114" cy="90" r="79" stroke-width="1.2"/>
        <circle cx="298" cy="122" r="79" stroke-width="1.2"/>
        <circle cx="479" cy="90" r="79" stroke-width="1.2"/>
      </g>
      <circle cx="114" cy="90" r="76" fill="var(--felt-mustard)" role="img" aria-label="Photo of an embroidered felt case with folk-art house and flowers"/>
      <circle cx="298" cy="122" r="76" fill="var(--felt-orange)" role="img" aria-label="Photo of an embroidered folk-art bird on orange wool"/>
      <circle cx="479" cy="90" r="76" fill="var(--felt-plum)" role="img" aria-label="Photo of an embroidered paisley motif on orange wool"/>
    </svg>
    <h1 class="name">ROSALIND HARKER</h1>
    <p class="role">Embroidery Designer &amp; Teacher</p>
  </section>

  <section class="card card-back">
    <div class="work-feature" role="img" aria-label="Photo of a purple wool book cover embroidered with colourful felt circles"></div>
    <ul class="contact">
      <li>PO BOX 3817</li>
      <li>ASHGROVE VALE SA 5092</li>
      <li>M: 0428361957</li>
      <li class="email">ROZ@COSYNEEDLEWORK.COM.AU</li>
    </ul>
  </section>

</div>
</body>
</html>
```